vantrel works cybersecurity website design and development

website design and development for a cybersecurity company. we have a logo and would like site to suit logo colors and look
cybersecurity website should be secure and look professional
main example of site we want to use: https://www.morvisquad.example/
site should be usable on tablet and phones

For each design proposal, please could you provide details of what language you'll use to code the website.

Target Market(s)

insurance companies, financial institutions, private SME, Africa and Europe

Coding

Coded - Design and coding required

Number of Pages Required

5+ page

Requirements
Must have
• 9 Pages:
Home
About us
Contacts
Partners
Blog
Services
( consulting, vulnerability assessment, information systems security audit, ISO compliance, Penetration testing, security awareness training, social engineering test, protection against DDoS, procurement )
Resources
Technologies
Careers
Nice to have
• nice to have all services have their own pages.
design based on logo colors and look

please provide what will be use to code the website

```html
<!DOCTYPE html>
<html lang="en">
<head>
<meta charset="utf-8">
<title>Vantrel Works — Cybersecurity</title>
<link href="https://fonts.googleapis.com/css2?family=Oswald:wght@300;400&family=Poppins:wght@400;500;600&display=swap" rel="stylesheet">
<style>
:root{
  --blue:#1565d8;
  --blue-deep:#0f3fae;
  --blue-light:#1a8fe8;
  --navy:#1e3a9a;
  --steel:#b4c7d6;
  --ink:#2b2b2b;
  --muted:#6d6d6d;
  --dark:#333639;
  --tile:#f3f4f5;
  --white:#ffffff;
}
*{margin:0;padding:0;box-sizing:border-box}
html,body{width:1200px;height:4142px;overflow:hidden}
body{position:relative;font-family:'Poppins',sans-serif;color:var(--ink);background:var(--white)}
.abs{position:absolute}
.heading{font-family:'Oswald',sans-serif;font-weight:400;text-transform:uppercase;letter-spacing:-.5px;color:var(--ink)}
.btn{position:absolute;display:flex;align-items:center;justify-content:center;font-size:12px;font-weight:600;text-transform:uppercase;border-radius:3px;color:var(--white);letter-spacing:.3px}
.btn-blue{background:linear-gradient(90deg,var(--blue-deep),var(--blue-light))}
.btn-navy{background:var(--navy)}
.btn-white{background:var(--white);color:var(--blue)}
/* header */
.site-header{left:0;top:0;width:1200px;height:92px;background:var(--white)}
.brand{left:88px;top:20px;display:flex;align-items:center;gap:10px}
.brand-mark{width:50px;height:50px;border-radius:50%;background:var(--blue)}
.brand-name{font-size:24px;font-weight:600;color:var(--blue)}
.main-nav{top:40px;font-size:12px;font-weight:500;text-transform:uppercase;color:#444}
/* hero */
.hero-copy{left:90px;top:240px;color:var(--white)}
.hero-title{font-family:'Oswald',sans-serif;font-size:84px;line-height:76px;font-weight:400;color:var(--white)}
.hero-text{font-size:15px;line-height:22px;width:340px;margin-top:14px}
.hero-art{left:520px;top:120px;width:660px;height:460px;border-radius:8px;background:radial-gradient(circle at 50% 45%,rgba(120,220,255,.55),rgba(30,110,220,.15) 60%,transparent 75%)}
.dot{position:absolute;top:743px;width:9px;height:9px;border-radius:50%;background:rgba(0,40,120,.6)}
/* generic */
.para{font-size:14px;line-height:23px;color:var(--muted)}
.underline{height:2px;width:52px;background:var(--steel)}
/* services */
.service-card{top:1464px;width:285px;height:404px;background:var(--white);box-shadow:0 8px 30px rgba(0,0,0,.1)}
.service-img{height:220px;background:linear-gradient(135deg,#12346d,#2b7fd4 60%,#7fb8e8)}
.service-body{padding:24px 24px}
.service-title{font-size:24px;margin-bottom:10px}
.service-text{font-size:13.5px;line-height:20px;color:var(--muted)}
.view-link{margin-top:24px;font-size:20px;font-weight:600;color:#b9bcc0;border-bottom:3px solid #e2e4e6;width:80px;padding-bottom:2px}
/* blog */
.blog-card{top:2810px;width:280px;height:375px;background:var(--white);box-shadow:0 8px 28px rgba(0,0,0,.1)}
.blog-img{height:210px;background:linear-gradient(135deg,#0c1e3c,#1f5fa8 55%,#6aa6d8)}
.blog-body{padding:22px 32px}
.blog-meta{font-size:12px;color:#555}
.blog-title{font-family:'Oswald',sans-serif;font-size:19px;line-height:27px;text-transform:uppercase;margin:8px 0 14px;font-weight:300;color:#222}
.pill{display:inline-block;font-size:10px;font-weight:500;padding:6px 12px;border-radius:14px;background:#eceeef;margin-right:4px}
/* trusted */
.partner{top:3415px;width:198px;height:77px;background:var(--tile);border:1px solid #e3e4e6;display:flex;align-items:center;justify-content:center;gap:8px;font-size:17px;font-weight:600;color:#333}
.partner i{width:22px;height:22px;border-radius:50%;background:var(--blue);display:block}
/* footer */
.footer-col{top:3790px}
.footer-col h4{font-family:'Oswald',sans-serif;font-weight:400;font-size:20px;color:var(--white);text-transform:uppercase;margin-bottom:14px}
.footer-col li{list-style:none;font-size:12.5px;color:#d8d8d8;line-height:23px}
.footer-col li::before{content:"› ";color:#888}
.contact-row{display:flex;gap:12px;font-size:12.5px;color:#d8d8d8;line-height:17px;margin-bottom:16px}
.social{top:3951px;width:29px;height:29px;border-radius:50%;border:1px solid #888}
</style>
</head>
<body>

<!-- backgrounds -->
<svg class="abs" style="left:0;top:0" width="1200" height="4142" aria-hidden="true">
  <defs>
    <linearGradient id="heroGrad" x1="0" y1="0" x2="1" y2="1">
      <stop offset="0" stop-color="#1a7fe0"/><stop offset="1" stop-color="#0e3cae"/>
    </linearGradient>
    <linearGradient id="techGrad" x1="0" y1="0" x2="1" y2="1">
      <stop offset="0" stop-color="#0e3a9e"/><stop offset="1" stop-color="#1e8ee8"/>
    </linearGradient>
  </defs>
  <polygon points="0,640 600,836 1200,640 1200,600 0,600" fill="#b4c7d6"/>
  <polygon points="0,92 1200,92 1200,625 600,820 0,625" fill="url(#heroGrad)"/>
  <polygon points="0,2520 282,2650 1200,2360 1200,2340 0,2340" fill="#b4c7d6"/>
  <polygon points="0,1990 1200,1990 1200,2350 282,2630 0,2500" fill="url(#techGrad)"/>
  <polygon points="0,3790 600,3600 1200,3790 1200,4142 0,4142" fill="#b4c7d6"/>
  <polygon points="0,3812 600,3622 1200,3812 1200,4142 0,4142" fill="#333639"/>
  <line x1="88" y1="4088" x2="1112" y2="4088" stroke="#555" stroke-width="1"/>
</svg>

<!-- header -->
<header class="abs site-header">
  <div class="abs brand"><span class="brand-mark"></span><span class="brand-name">Vantrel Works</span></div>
  <nav>
    <span class="abs main-nav" style="left:415px">About us</span>
    <span class="abs main-nav" style="left:505px">Services</span>
    <span class="abs main-nav" style="left:590px">Technologies</span>
    <span class="abs main-nav" style="left:711px">Careers</span>
    <span class="abs main-nav" style="left:793px">Resources</span>
    <span class="abs main-nav" style="left:892px">Blog</span>
    <span class="abs main-nav" style="left:952px">Partners</span>
    <span class="abs main-nav" style="left:1042px">Contacts</span>
  </nav>
</header>

<!-- hero -->
<section>
  <div class="abs hero-art" role="img" aria-label="Isometric illustration of a glowing fingerprint scanner surrounded by a padlock, servers, laptop, phone and cloud on a circuit board"></div>
  <div class="abs hero-copy">
    <h1 class="hero-title">ARE YOU<br>CYBERSECURE</h1>
    <p class="hero-text">Would you be able to detect automated or targeted attacks? Do you know if have you already been a victim?</p>
  </div>
  <a class="btn btn-blue" style="left:90px;top:491px;width:141px;height:38px;background:#1a8fe8">Learn more</a>
  <span class="dot" style="left:576px"></span>
  <span class="dot" style="left:591px;width:11px;height:11px;top:742px;background:#fff"></span>
  <span class="dot" style="left:608px"></span>
</section>

<!-- tagline -->
<p class="abs" style="left:0;top:880px;width:1200px;text-align:center;font-size:22px;line-height:32px;color:#333">We make sure our clients stay ahead of attacks<br>and mitigate future risks</p>

<!-- about -->
<section>
  <div class="abs" role="img" aria-label="Silver shield emblem with a blue padlock" style="left:175px;top:997px;width:390px;height:378px;border-radius:40px 40px 50% 50%;background:linear-gradient(160deg,#e8eef3,#a9bccb)"></div>
  <h2 class="abs heading" style="left:618px;top:1035px;font-size:48px">About Vantrel Works</h2>
  <div class="abs underline" style="left:618px;top:1098px"></div>
  <p class="abs para" style="left:618px;top:1118px;width:410px">Aenean sollicitudin lorem quis bibendum auctor nisi elit consequat ipsum, nec sagittis sem nibh id elit duis sed odio sit amet nibh vulputate cursus a sit amet mauris. Morbi accumsan ipsum velit. Nam nec tellus a odi ornare odio. Sed non mauris vitae erat consequat auctor eu in elit. Class aptent taciti sociosqu....</p>
  <a class="btn btn-navy" style="left:618px;top:1282px;width:115px;height:40px">Learn more</a>
</section>

<!-- services -->
<section>
  <h2 class="abs heading" style="left:88px;top:1555px;font-size:48px">Our Services</h2>
  <p class="abs para" style="left:88px;top:1633px;width:300px;font-size:13.5px">Aenean sollicitudin lorem quis nec nibh vulputate cursus a sit amet maurisMorbi accumsan ipsum velit.</p>
  <a class="btn btn-blue" style="left:88px;top:1722px;width:153px;height:40px">View all service</a>

  <article class="abs service-card" style="left:428px">
    <div class="service-img" role="img" aria-label="Hand touching a glowing consulting interface"></div>
    <div class="service-body">
      <h3 class="heading service-title">Consulting</h3>
      <p class="service-text">Aenean sollicitudin lorem quis nec nibh vulputate cursus a sit amet mauris Morbi</p>
      <div class="view-link">View</div>
    </div>
  </article>
  <article class="abs service-card" style="left:727px">
    <div class="service-img" role="img" aria-label="Finger pressing an ISO standards hologram"></div>
    <div class="service-body">
      <h3 class="heading service-title">ISO Compliance</h3>
      <p class="service-text">Aenean sollicitudin lorem quis nec nibh vulputate cursus a sit amet mauris Morbi</p>
      <div class="view-link">View</div>
    </div>
  </article>
  <article class="abs service-card" style="left:1025px">
    <div class="service-img" role="img" aria-label="Hands holding a procurement location pin icon" style="background:linear-gradient(135deg,#2c3d5c,#6c87ad)"></div>
    <div class="service-body">
      <h3 class="heading service-title">Procurement</h3>
      <p class="service-text" style="white-space:nowrap">Aenean sollicitudin lorem<br>nec nibh vulputate cursus<br>amet mauris Morbi</p>
      <div class="view-link">View</div>
    </div>
  </article>
</section>

<!-- technologies -->
<section>
  <div class="abs" role="img" aria-label="Isometric illustration of a laptop, data towers and people working with charts" style="left:0;top:2000px;width:640px;height:560px;background:radial-gradient(circle at 45% 45%,rgba(80,170,255,.45),transparent 70%)"></div>
  <h2 class="abs heading" style="left:705px;top:2080px;font-size:46px;color:#fff">Technologies</h2>
  <div class="abs underline" style="left:705px;top:2143px;background:rgba(255,255,255,.5)"></div>
  <p class="abs para" style="left:705px;top:2163px;width:410px;color:#fff">Aenean sollicitudin lorem quis bibendum auctor nisi elit consequat ipsum, nec sagittis sem nibh id elit duis sed odio sit amet nibh vulputate cursus a sit amet mauris. Morbi accumsan ipsum velit. Nam nec tellus a odi ornare odio. Sed non mauris vitae erat consequat auctor eu in elit. Class aptent taciti sociosqu....</p>
  <a class="btn btn-white" style="left:705px;top:2326px;width:115px;height:40px">Learn more</a>
</section>

<!-- blog -->
<section>
  <h2 class="abs heading" style="left:0;top:2718px;width:1200px;text-align:center;font-size:48px">Latest Blog Post</h2>
  <article class="abs blog-card" style="left:165px">
    <div class="blog-img" role="img" aria-label="Hands typing on a laptop with a padlock hologram"></div>
    <div class="blog-body"><p class="blog-meta">byMaren &nbsp;•&nbsp; January 2021</p><h3 class="blog-title">Some blog heading goes<br>here with des...</h3><span class="pill">41 COMMENT</span><span class="pill">25 LIKES</span></div>
  </article>
  <article class="abs blog-card" style="left:460px">
    <div class="blog-img" role="img" aria-label="Businessman touching a circuit padlock interface"></div>
    <div class="blog-body"><p class="blog-meta">byMaren &nbsp;•&nbsp; January 2021</p><h3 class="blog-title">Some blog heading goes<br>here with des...</h3><span class="pill">41 COMMENT</span><span class="pill">25 LIKES</span></div>
  </article>
  <article class="abs blog-card" style="left:756px">
    <div class="blog-img" role="img" aria-label="Hands on a glowing blue keyboard"></div>
    <div class="blog-body"><p class="blog-meta">byMaren &nbsp;•&nbsp; January 2021</p><h3 class="blog-title">Some blog heading goes<br>here with des...</h3><span class="pill">41 COMMENT</span><span class="pill">25 LIKES</span></div>
  </article>
</section>

<!-- trusted -->
<section>
  <h2 class="abs heading" style="left:0;top:3310px;width:1200px;text-align:center;font-size:48px">They Already Trusted Us</h2>
  <span class="abs" style="left:1062px;top:3330px;font-size:18px;color:#555">‹</span>
  <span class="abs" style="left:1088px;top:3330px;font-size:18px;color:#555">›</span>
  <div class="abs partner" style="left:88px"><i></i>Company</div>
  <div class="abs partner" style="left:297px"><i></i>Loopwise</div>
  <div class="abs partner" style="left:502px"><i></i>Nordafel</div>
  <div class="abs partner" style="left:708px"><i></i>Peakline</div>
  <div class="abs partner" style="left:914px"><i></i>Tesmo</div>
</section>

<!-- footer -->
<footer>
  <div class="abs" style="left:100px;top:3875px;display:flex;align-items:center;gap:12px">
    <span style="width:66px;height:66px;border-radius:50%;background:var(--blue);display:block"></span>
    <span style="font-size:26px;font-weight:600;color:var(--blue-light)">Vantrel Works</span>
  </div>
  <span class="abs social" style="left:182px"></span>
  <span class="abs social" style="left:220px"></span>
  <span class="abs social" style="left:258px"></span>
  <span class="abs social" style="left:296px"></span>

  <div class="abs footer-col" style="left:433px">
    <h4>Useful Links</h4>
    <ul><li>Home</li><li>About us</li><li>Services</li><li>Technologies</li><li>Careers</li><li>Resources</li><li>Blog</li><li>Partners</li><li>Contacts</li></ul>
  </div>
  <div class="abs footer-col" style="left:640px">
    <h4>Our Services</h4>
    <ul><li>Consulting</li><li>Culnerability assessment</li><li>Information systems security audit</li><li>ISO compliance</li><li>Penetration testing</li><li>Security awareness training</li><li>Social engineering test</li><li>Protection against DDoS</li><li>Procurement</li></ul>
  </div>
  <div class="abs footer-col" style="left:920px">
    <h4>Contact Us</h4>
    <div class="contact-row"><svg width="10" height="14" viewBox="0 0 10 14"><path d="M5 0a5 5 0 0 0-5 5c0 4 5 9 5 9s5-5 5-9a5 5 0 0 0-5-5zm0 7a2 2 0 1 1 0-4 2 2 0 0 1 0 4z" fill="#999"/></svg><span>Harbor Row, 12245<br>United States</span></div>
    <div class="contact-row"><svg width="12" height="12" viewBox="0 0 12 12"><path d="M2.4 0l2 2.6-1.2 1.5a7 7 0 0 0 4.7 4.7l1.5-1.2L12 9.6 10.4 12A10.5 10.5 0 0 1 0 1.6z" fill="#999"/></svg><span>Phone:<br>+123 456 7890</span></div>
    <div class="contact-row"><svg width="12" height="10" viewBox="0 0 12 10"><rect width="12" height="10" rx="1" fill="#999"/><path d="M0 1l6 4 6-4" stroke="#333" fill="none"/></svg><span>Email:<br>youremail@domain.com</span></div>
  </div>

  <p class="abs" style="left:0;top:4106px;width:1200px;text-align:center;font-size:11px;font-weight:500;color:#e0e0e0">© COPYRIGHT 2021 VANTREL WORKS ALL RIGHTS RESERVED</p>
  <svg class="abs" style="left:1130px;top:4076px" width="48" height="48" viewBox="0 0 48 48" aria-label="Chat">
    <circle cx="24" cy="24" r="23" fill="#1a7fe0"/>
    <path d="M15 18a4 4 0 0 1 4-4h10a4 4 0 0 1 4 4v7a4 4 0 0 1-4 4h-7l-5 4v-4a4 4 0 0 1-2-3.5z" fill="#fff"/>
  </svg>
</footer>

</body>
</html>
```